Exceptional Corporate Business Card Design

Hello,

We need an exceptional corporate business card design based on our logo attached. We require:

1. A Variation for letterpress print
2. Standard size of business card 84mm x 55mm (Artwork 88mm x 59mm)
3. Variation for square business card 65mm x 65mm (Artwork 69mm x 69mm)
4. Variation as a one side print
5. Adobe Illustrator files

The company is in the financial industry, valmisto.com

The logo is attached as vector pdf.
regards

```html
<!DOCTYPE html>
<html lang="en">
<head>
<meta charset="utf-8">
<title>Valmisto Business Card</title>
<link rel="stylesheet" href="https://fonts.googleapis.com/css2?family=PT+Sans:ital,wght@0,400;0,700;1,400&display=swap">
<style>
  :root {
    --stage: #3c3c3c;
    --card-light: #f6f6f6;
    --brand: #2e2278;
    --ink: #444448;
    --white: #ffffff;
  }
  * { margin: 0; padding: 0; box-sizing: border-box; }
  html, body { width: 1200px; height: 750px; overflow: hidden; }
  body {
    background: var(--stage);
    font-family: "PT Sans", sans-serif;
    position: relative;
  }
  .card {
    position: absolute;
    top: 228px;
    width: 491px;
    height: 280px;
    border-radius: 16px;
    overflow: hidden;
  }
  .card--front { left: 106px; background: var(--card-light); }
  .card--back { left: 609px; background: var(--brand); }

  .name-band {
    position: absolute;
    left: 0; top: 37px;
    width: 276px; height: 82px;
    background: var(--brand);
    color: var(--white);
    padding: 22px 0 0 38px;
  }
  .person-name { font-size: 18px; font-weight: 700; line-height: 1.1; }
  .person-role { font-size: 13px; margin-top: 5px; }

  .brand-lockup {
    position: absolute;
    left: 244px; top: 37px;
    height: 82px;
    display: flex; align-items: center; gap: 6px;
    white-space: nowrap;
  }
  .brand-dot {
    width: 82px; height: 82px; border-radius: 50%;
    background: var(--card-light);
    border: 5px solid var(--brand);
    flex: none;
  }
  .brand-name {
    font-size: 26px; font-weight: 700; color: var(--brand);
    line-height: 1;
    white-space: nowrap;
  }

  .contact {
    position: absolute;
    top: 219px;
    font-size: 12.5px;
    color: var(--ink);
    line-height: 19px;
    white-space: nowrap;
  }
  .contact--address { left: 38px; top: 221px; }
  .contact--phone { left: 194px; }
  .contact--web { left: 314px; }
  .contact-row { display: flex; align-items: center; gap: 7px; }
  .contact-row svg { width: 12px; height: 12px; fill: var(--brand); flex: none; }

  .back-mark {
    position: absolute;
    left: 159px; top: 47px;
    width: 172px; height: 172px;
    border-radius: 50%;
    border: 6px solid var(--white);
    display: flex; align-items: center; justify-content: center;
  }
  .back-mark .brand-name { color: var(--white); font-size: 28px; }
  .back-url {
    position: absolute;
    left: 0; right: 0; top: 238px;
    display: flex; align-items: center; justify-content: center; gap: 10px;
    color: var(--white);
    font-style: italic; font-size: 12px; letter-spacing: 4px;
  }
  .back-url .rule {
    width: 44px; height: 2px;
    background: linear-gradient(90deg, transparent, var(--white));
  }
  .back-url .rule--right { background: linear-gradient(90deg, var(--white), transparent); }
</style>
</head>
<body>
  <section class="card card--front">
    <div class="name-band">
      <p class="person-name">John Smith</p>
      <p class="person-role">Director</p>
    </div>
    <div class="brand-lockup">
      <span class="brand-dot"></span>
      <span class="brand-name">VALMISTO</span>
    </div>

    <div class="contact contact--address">
      <p>Suite 102 Street name</p>
      <p>State, Zip 2034,Country</p>
    </div>
    <div class="contact contact--phone">
      <p class="contact-row">
        <svg viewBox="0 0 12 12"><path d="M1 4c0-2 2-3 5-3s5 1 5 3l-2 1-1-1H4L3 5zM2 7l2-2h4l2 2v4H2z"/></svg>
        127 345 9876
      </p>
      <p class="contact-row">
        <svg viewBox="0 0 12 12"><path d="M3 1h6v3H3zM1 5h10v5H9v-2H3v2H1zM4 9h4v3H4z"/></svg>
        345 345 9876
      </p>
    </div>
    <div class="contact contact--web">
      <p class="contact-row">
        <svg viewBox="0 0 12 12"><path d="M0 2h12v1L6 7 0 3zM0 4l6 4 6-4v6H0z"/></svg>
        info@yourname.com
      </p>
      <p class="contact-row">
        <svg viewBox="0 0 12 12"><circle cx="6" cy="6" r="5" fill="none" stroke="#2e2278" stroke-width="1.2"/><path d="M1 6h10M6 1v10" stroke="#2e2278" stroke-width="1" fill="none"/></svg>
        www.yourname.com
      </p>
    </div>
  </section>

  <section class="card card--back">
    <div class="back-mark">
      <span class="brand-name">VALMISTO</span>
    </div>
    <p class="back-url">
      <span class="rule"></span>www.yourweb.com<span class="rule rule--right"></span>
    </p>
  </section>
</body>
</html>
```